Mini Leporello with Tartar Recipe from Christmas Apéro

As present from our christmas apero we would like to give our visitors a little booklet of the tartar recipes they enjoyed with us. For this we need a little pocket recipe booklet. ISt should be a Mini-Leparello. You can find the content attached.

Target Market(s)

customers christmas apero

Font styles to use
Other font styles liked:
• FS albert

Requirements
Must have
• each recipe comes from Velmar or Markus Tobler - it should show the author
• the format should be 85 x 85 mm and I need a printable file

```html
<!DOCTYPE html>
<html lang="de">
<head>
<meta charset="utf-8">
<title>Tartar-Rezepte vom Brenner – Leporello</title>
<link href="https://fonts.googleapis.com/css2?family=Nunito+Sans:wght@400;600;800&display=swap" rel="stylesheet">
<style>
  :root{
    --red:#e3141c;
    --white:#ffffff;
    --ink:#2b2b2b;
    --bg:#e6e6e6;
  }
  *{box-sizing:border-box;margin:0;padding:0}
  html,body{width:1200px;height:900px;overflow:hidden;background:var(--bg)}
  body{font-family:"Nunito Sans",sans-serif;color:var(--ink);position:relative}
  .strip{position:absolute;left:72px;width:1056px;height:264px;background:var(--red);display:flex}
  .strip--front{top:156px}
  .strip--back{top:456px}
  .panel{position:relative;width:264px;height:264px}
  .sheet{position:absolute;inset:6px;background:var(--white)}
  .frame{position:absolute;inset:3px;border:1px solid var(--red);pointer-events:none}
  .photo{position:absolute;left:10px;top:8px;width:228px;height:122px}
  .rule-h{position:absolute;left:4px;right:4px;top:140px;height:1px;background:#8a8a8a}
  .rule-v{position:absolute;left:108px;top:140px;width:1px;height:104px;background:#8a8a8a}
  .title{position:absolute;left:12px;top:148px;color:var(--red);font-weight:800;font-size:14px;line-height:17px}
  .desc{position:absolute;left:12px;width:92px;font-size:6.6px;line-height:8.8px}
  .ingredients{position:absolute;left:118px;top:150px;display:flex;gap:10px;font-size:8.6px;line-height:11px}
  .ingredients ul{list-style:none}
  .ingredients li::before{content:"• "}
  .ingredients .note{font-size:6px;line-height:7.5px;margin-top:3px;width:112px}
  .brand{position:absolute;color:var(--red);font-weight:800;font-size:16px;line-height:1}
  .shop{position:absolute;display:flex;align-items:center;gap:4px;color:var(--red);font-weight:800;font-size:11px}
  .shop::before{content:"";width:10px;height:10px;background:var(--red)}
  /* cover */
  .cover-head{position:absolute;left:14px;right:14px;top:30px;text-align:center;color:var(--red)}
  .cover-head .line{display:flex;align-items:center;gap:6px;height:10px}
  .cover-head .line span{flex:1;height:1px;background:var(--red)}
  .cover-head .ring{width:7px;height:7px;border:1px solid var(--red);border-radius:50%}
  .cover-title{font-weight:800;font-size:26px;line-height:28px;letter-spacing:.5px}
  .cover-sub{font-size:10px;letter-spacing:8.4px;margin-top:2px}
  .cover-year{font-weight:800;font-size:12px;letter-spacing:4px}
  .credit{position:absolute;left:0;right:0;bottom:4px;text-align:center;font-size:7.2px}
  .url{position:absolute;left:0;right:0;bottom:6px;text-align:center;font-size:7.2px}
</style>
</head>
<body>

<section class="strip strip--front">
  <article class="panel">
    <div class="sheet">
      <div class="frame"></div>
      <header class="cover-head">
        <div class="line"><span></span><i class="ring"></i><span></span></div>
        <h1 class="cover-title">TARTAR-REZEPTE<br>VOM BRENNER</h1>
        <p class="cover-sub">WEIHNACHTSAPÉRO</p>
        <div class="line"><span></span><b class="cover-year">2016</b><span></span></div>
      </header>
      <div class="brand" style="left:30px;top:164px;font-size:19px">Brenner</div>
      <div class="shop" style="left:154px;top:166px;font-size:13px">Velmar</div>
      <p class="credit">each recipe comes from Velmar or Markus Tobler</p>
    </div>
  </article>

  <article class="panel">
    <div class="sheet">
      <div class="frame"></div>
      <div class="photo" role="img" aria-label="Foto: Rindertartar mit Salat und Brot" style="background:linear-gradient(90deg,#4f6a2c 0%,#b2203a 30%,#a3142f 60%,#c99458 100%)"></div>
      <div class="rule-h"></div><div class="rule-v"></div>
      <h2 class="title">Rindertartar</h2>
      <p class="desc" style="top:190px">Alle Zutaten fein hacken und mischen:</p>
      <div class="ingredients">
        <ul><li>Rindsfilet</li><li>Essiggurken</li><li>Oliven</li><li>Peperoni</li><li>Kapern</li></ul>
        <ul><li>Zwiebel</li><li>Essig</li><li>Senf</li><li>Pfeffer</li><li>Salz</li></ul>
      </div>
      <div class="shop" style="left:192px;top:226px">Velmar</div>
    </div>
  </article>

  <article class="panel">
    <div class="sheet">
      <div class="frame"></div>
      <div class="photo" role="img" aria-label="Foto: Ligurisches Kalbstartar auf grüner Sauce" style="background:radial-gradient(ellipse at 55% 55%,#6a3b2b 0%,#4d6e1c 40%,#2f3c12 75%,#6f6a5a 100%)"></div>
      <div class="rule-h"></div><div class="rule-v"></div>
      <h2 class="title">Ligurisches<br>Kalbstartar</h2>
      <p class="desc" style="top:190px">Alle Zutaten fein hacken und mischen:</p>
      <div class="ingredients">
        <ul><li>Kalbfleisch</li><li>Zitronen</li><li>Olivenoel</li><li>Grosszügig Parmesansplitter</li></ul>
      </div>
      <div class="ingredients" style="left:183px">
        <ul><li>Knoblauch</li><li>Pfeffer</li><li>Salz</li></ul>
      </div>
      <div class="brand" style="right:14px;top:222px">Brenner</div>
    </div>
  </article>

  <article class="panel">
    <div class="sheet">
      <div class="frame"></div>
      <div class="photo" role="img" aria-label="Foto: Tomatentartar mit Kräutern" style="background:radial-gradient(ellipse at 50% 55%,#b4321c 0%,#d9694a 30%,#f1d8e2 60%,#f8eef3 100%)"></div>
      <div class="rule-h"></div><div class="rule-v"></div>
      <h2 class="title">Tomatentartar</h2>
      <p class="desc" style="top:168px;font-size:5.3px;line-height:7.8px">Im Prinzip ist das Tomatentartar ein klassisches Rindstartar, anstelle des Fleisches nimmt man einfach getrocknete / in Oel eingelegte Tomaten. Giessen Sie den Grossteils des Oels ab, aber tupfen Sie die Tomaten nicht trocken. Zerkleinern Sie die Tomaten dann mit dem Pürierstab (nicht zu fein) und geben folgende Zutaten hinzu:</p>
      <div class="ingredients" style="font-size:8.2px;gap:4px">
        <ul><li>Eigelb</li><li>Kapern</li><li>Basilikum</li><li>Cognac</li><li>Pfeffer</li><li>Salz</li></ul>
        <ul><li>Weitere Gewürze<br>&nbsp;&nbsp;nach Abschmecken,<br>&nbsp;&nbsp;bzw. je nach Wür-<br>&nbsp;&nbsp;zigkeit der im Oel<br>&nbsp;&nbsp;eingelegten Tomaten</li></ul>
      </div>
      <div class="brand" style="right:14px;top:222px">Brenner</div>
    </div>
  </article>
</section>

<section class="strip strip--back">
  <article class="panel">
    <div class="sheet">
      <div class="frame"></div>
      <div class="photo" role="img" aria-label="Foto: Thunatartar mit Sprossen und Sojasauce" style="background:radial-gradient(ellipse at 50% 50%,#c5434a 0%,#9f3a35 35%,#d6d3cc 70%,#8d8b84 100%)"></div>
      <div class="rule-h"></div><div class="rule-v"></div>
      <h2 class="title">Thunatartar<br>Asiatisch</h2>
      <p class="desc" style="top:188px">Dieses Thunatartar bekommt mit folgenden Zutaten eine asiatische Note:</p>
      <div class="ingredients" style="top:144px">
        <ul><li>Zitronengras</li><li>Ingwer</li><li>Basilikum</li><li>Koriander</li><li>Etwas Sojasauce mit Wasabi</li>
          <li class="note" style="list-style:none">Fügen Sie weitere asiatische Saucen gemäss Ihrem Geschmack individuell bei.</li></ul>
      </div>
      <div class="brand" style="right:14px;top:222px">Brenner</div>
    </div>
  </article>

  <article class="panel">
    <div class="sheet">
      <div class="photo" role="img" aria-label="Foto: Lachstartar mit Gurke" style="background:linear-gradient(180deg,#b9bfd6 0%,#e59a78 35%,#f1efe6 55%,#b9c67a 75%,#e6e8ef 100%)"></div>
      <div class="rule-h"></div><div class="rule-v"></div>
      <h2 class="title">Lachstartar</h2>
      <p class="desc" style="top:190px">Geräuchter Lachs fein hacken und mit allen Zutaten mischen.</p>
      <div class="ingredients">
        <ul><li>Geräuchter Lachs</li><li>Sauerrahm</li><li>Dill</li></ul>
      </div>
      <div class="shop" style="left:192px;top:226px">Velmar</div>
    </div>
  </article>

  <article class="panel">
    <div class="sheet">
      <div class="photo" role="img" aria-label="Foto: Käsetartar angerichtet" style="background:radial-gradient(ellipse at 50% 50%,#c5434a 0%,#9f3a35 35%,#d6d3cc 70%,#8d8b84 100%)"></div>
      <div class="rule-h"></div><div class="rule-v"></div>
      <h2 class="title">Käsetartar</h2>
      <p class="desc" style="top:170px;line-height:9.2px">Den Käse entrinden und in kleine Würfelchen schneiden, Lauch blanchieren, kalt abschrecken. Petersilie und Radieschen hacken danach alle Zutaten mischen und anrichten.</p>
      <div class="ingredients">
        <ul><li>Halbhartkäse</li><li>Radieschen</li><li>Lauch</li><li>Weinessig</li><li>Senf</li></ul>
        <ul><li>Schwarzer<br>&nbsp;&nbsp;Pfeffer</li><li>Rapsöl</li><li>Rahm</li><li>Petersilie<br>&nbsp;&nbsp;Glattblätterig</li></ul>
      </div>
      <div class="shop" style="left:130px;top:226px">Velmar</div>
    </div>
  </article>

  <article class="panel">
    <div class="sheet">
      <div class="brand" style="left:38px;top:112px;font-size:19px">Brenner</div>
      <div class="shop" style="left:158px;top:114px;font-size:13px">Velmar</div>
      <p class="url">www.velmar.ch/de/feinkost</p>
    </div>
  </article>
</section>

</body>
</html>
```